Design for Chirpwall Ad to promote Laptops purchase

Need a graphic design for a Chirpwall Ad - to promote 2 laptops (PC and Zorvane) with the stated required ad-text.

AD TEXT:

FOR SME BUSINESS ONLY!
Chat with us!
To get advice on how to apply
and defray up to 80%* of business laptop purchase cost!

*Terms and Conditions apply

Image for reference only

Target Market(s)

Small medium business

Font styles to use
Sans Serif

Requirements
Must have
• 2 laptop images (see attached ) - 1 vector image of ZORVANE , and pls try to create another vector image of PC laptop (where screen is showing Blue Pendrel screen)

```html
<!DOCTYPE html>
<html lang="en">
<head>
<meta charset="utf-8">
<title>SME Business Laptop Ad</title>
<link href="https://fonts.googleapis.com/css2?family=Playfair+Display:ital@1&family=Poppins:wght@600&family=Fredoka:wght@500&family=Nunito+Sans:wght@400;700&display=swap" rel="stylesheet">
<style>
  :root {
    --canvas: #ffffff;
    --panel-light: #f0f0f0;
    --panel-grey: #7f858e;
    --chevron-dark: #636363;
    --frame: #8a8a8a;
    --accent: #f7941d;
    --ink: #333333;
    --ink-soft: #4a4a4a;
  }
  html, body {
    margin: 0;
    padding: 0;
    width: 1200px;
    height: 1200px;
    overflow: hidden;
    background: var(--canvas);
  }
  .ad-banner {
    position: absolute;
    left: 87px;
    top: 341px;
    width: 1020px;
    height: 533px;
    background: var(--panel-light);
    outline: 1px solid var(--frame);
    overflow: hidden;
  }
  .product-panel {
    position: absolute;
    left: 0;
    top: 0;
  }
  .headline-lead,
  .headline-tail {
    position: absolute;
    left: 62px;
    margin: 0;
    font-family: "Playfair Display", Georgia, serif;
    font-style: italic;
    font-weight: 400;
    font-size: 48px;
    color: var(--ink);
    line-height: 1;
  }
  .headline-lead { top: 56px; }
  .headline-tail { top: 186px; }
  .headline-main {
    position: absolute;
    left: 61px;
    top: 122px;
    margin: 0;
    font-family: "Poppins", Arial, sans-serif;
    font-weight: 600;
    font-size: 46px;
    letter-spacing: -1px;
    color: var(--accent);
    line-height: 1;
  }
  .chat-button {
    position: absolute;
    left: 62px;
    top: 284px;
    width: 274px;
    height: 45px;
    background: var(--accent);
    color: #ffffff;
    font-family: "Fredoka", Arial, sans-serif;
    font-weight: 500;
    font-size: 30px;
    letter-spacing: 1px;
    display: flex;
    align-items: center;
    justify-content: center;
  }
  .offer {
    position: absolute;
    left: 61px;
    top: 384px;
    font-family: "Nunito Sans", Arial, sans-serif;
    color: var(--ink);
  }
  .offer p { margin: 0; }
  .offer-intro,
  .offer-outro {
    font-size: 20px;
    line-height: 1.2;
  }
  .offer-highlight {
    font-weight: 700;
    font-size: 33px;
    color: var(--accent);
    line-height: 1.15;
    letter-spacing: 0.5px;
  }
  .fine-print {
    position: absolute;
    right: 5px;
    bottom: 5px;
    margin: 0;
    font-family: "Nunito Sans", Arial, sans-serif;
    font-size: 6px;
    color: var(--ink-soft);
  }
</style>
</head>
<body>
  <section class="ad-banner">
    <svg class="product-panel" width="1020" height="533" viewBox="0 0 1020 533">
      <defs>
        <linearGradient id="pcLaptopTone" x1="0" y1="0" x2="1" y2="1">
          <stop offset="0" stop-color="#1d3f7a"/>
          <stop offset="0.55" stop-color="#2f6fc4"/>
          <stop offset="1" stop-color="#c9cdd2"/>
        </linearGradient>
        <linearGradient id="zorvaneLaptopTone" x1="0" y1="0" x2="1" y2="1">
          <stop offset="0" stop-color="#5a2f78"/>
          <stop offset="0.5" stop-color="#c58fd6"/>
          <stop offset="1" stop-color="#d7d9dc"/>
        </linearGradient>
      </defs>
      <polygon class="chevron-band" points="541,0 1020,0 1020,533 541,533 476,264" fill="var(--chevron-dark)"/>
      <polygon class="grey-field" points="563,0 1020,0 1020,533 563,533 498,264" fill="var(--panel-grey)"/>
      <polygon class="grey-field-edge" points="563,0 1020,0 1020,533 563,533 498,264" fill="var(--panel-grey)"/>
      <rect x="576" y="36" width="347" height="218" rx="14" fill="url(#pcLaptopTone)" role="img" aria-label="Silver Pendrel business laptop showing a blue start screen"/>
      <rect x="608" y="289" width="353" height="190" rx="14" fill="url(#zorvaneLaptopTone)" role="img" aria-label="Silver Zorvane laptop with a purple space wallpaper"/>
    </svg>

    <p class="headline-lead">for</p>
    <h1 class="headline-main">SME BUSINESS</h1>
    <p class="headline-tail">Only!</p>

    <div class="chat-button">CHAT WITH US!</div>

    <div class="offer">
      <p class="offer-intro">To Get Advice on How To Apply &amp;</p>
      <p class="offer-highlight">Defray up to 80%*</p>
      <p class="offer-outro">of Business Laptop Purchase Cost!</p>
    </div>

    <p class="fine-print">Image for reference only &nbsp;|&nbsp; *Terms and Conditions apply</p>
  </section>
</body>
</html>
```